依頼詳細
載内容詳細に関しては、別添のExcel資料を参照してください。

・ターゲット
BtoB
マンションの管理組合や管理業者
BtoC
防水工事系の仕事経験者の方で仕事を探している方

・カラーイメージ
青系
ロゴで使用されている青色を使用して、デザインお願いします。
▼参考
https://www.harumizu-cycle.jp/

・デザイン、ムード
参考のように企業らしい堅めのイメージでデザインお願いします
▼参考
http://www.tomonaga-kiko.biz
https://www.seiran-kenchi.co.jp/

配置やデザイン等はアレンジしていただいて構いません。
また、縦に制限はありません。

レスポンシブデザインのサイトで、bootstrap4を利用しコーディングする予定になります。

デザイン幅は2000px、コンテンツの幅はbootstrap4デフォルトのの1110pxを基準としてください。
ただし、最近のデザインの流行を取りいれて、フルワイドや、1200~1500px程度の幅のコンテンツをバランスよくレイアウトしてください。
コンテンツ配置は基本12分割になります。がデザインによっては、多少逸脱してもかまいません。
bootstrap4、12分割グリッドの基準のPSDも資料として添付しております。
ご参考になさってください。

本分のフォントはゴシック系は游ゴシック、メイリオ、明朝系は遊明朝でお願いします。
飾り文字はフリーフォントか、googleフォントを利用してください。

メイン画像部分・グローバルメニューは、ワイド適用でお願いします。

不明点、質問などありましたらメッセージ等でご連絡ください。
サイトURL
ページ数
1ページ
希望イメージ
シンプル 複雑
単色 カラフル
暗い 明るい
日常 高級
遊び心 厳粛
未来的 伝統的
女性的 男性的
希望する色
青系、水色系
納品ファイル
• 高解像度JPG (.jpg)
• フォトショップ形式 (.psd)
補足説明
・資料上はサイト名(社名)や住所などは伏字にしております。
ご提案時点ではそのまま作成をお願いします。

・使用画像は当選後こちらで用意します。
ご提案時点では前項同様に、カンプデータ等をご使用のうえ、当選後に本内容へ差し替え修正をお願いします。
また、雰囲気が合っていれば、指定外の画像を追加掲載いただいてOKです。

・当選前提となった方は正式な社名及び連絡先をお伝えしますので修正対応をお願いします。

お客様が希望されていたデザインイメージにピッタリだったため。

数多くの素晴らしい提案をいただきありがとうございました。
また次回もご参加よろしくお願いいたします。

```html
<!DOCTYPE html>
<html lang="ja">
<head>
<meta charset="utf-8">
<title>株式会社〇〇〇〇</title>
<link rel="stylesheet" href="https://fonts.googleapis.com/css2?family=Noto+Sans+JP:wght@400;500;700&family=Noto+Serif+JP:wght@500;700&family=Cormorant+Garamond:wght@500;600&display=swap">
<style>
:root{
  --blue:#1a7fd6;
  --blue-deep:#1466b3;
  --sky:#dcefff;
  --sky-soft:#eef7ff;
  --ink:#333;
  --faint:#bfe0f7;
  --dark:#3a4650;
}
*{box-sizing:border-box;margin:0;padding:0}
html,body{width:1200px;height:2756px;overflow:hidden;background:#fff}
body{position:relative;font-family:"Noto Sans JP",sans-serif;color:var(--ink)}
.abs{position:absolute}

/* header */
.site-header{left:0;top:0;width:1200px;height:68px;background:#fff;display:flex;align-items:center;padding:0 0 0 20px;z-index:5}
.brand{display:flex;align-items:center;gap:12px;font-weight:700;font-size:22px;color:var(--ink)}
.brand-dot{width:36px;height:36px;border-radius:50%;background:var(--blue)}
.global-nav{margin-left:auto;display:flex;align-items:center;height:68px}
.global-nav a{font-size:15px;color:var(--ink);text-decoration:none;padding:0 26px;font-weight:500}
.tel-btn{background:var(--blue);color:#fff!important;height:68px;display:flex;align-items:center;gap:8px;padding:0 34px!important;font-size:17px!important}

/* hero */
.hero{left:0;top:68px;width:1200px;height:592px;background:linear-gradient(90deg,#fff 0%,#f1f8fd 30%,#cfe3f1 45%,#b9d6ea 100%)}
.hero-photo{left:460px;top:0;width:740px;height:592px;background:linear-gradient(180deg,#cfe4f4 0%,#a9c8df 45%,#c8d8c6 78%,#b8c7b0 100%)}
.hero-fade{left:380px;top:0;width:200px;height:592px;background:linear-gradient(90deg,#f1f8fd,rgba(241,248,253,0))}
.hero-copy{left:70px;top:345px;font-family:"Noto Serif JP",serif;font-weight:700;color:var(--blue);line-height:1.35}
.hero-copy .l1{font-size:46px;background:rgba(255,255,255,.75);padding:0 6px}
.hero-copy .l2{font-size:40px;background:rgba(255,255,255,.75);padding:0 6px;display:inline-block;margin-top:8px}

/* section headings */
.sec-title{display:flex;align-items:flex-end;gap:18px}
.sec-title .en{font-family:"Cormorant Garamond",serif;font-size:120px;line-height:.8;color:var(--faint);font-weight:500}
.sec-title .ja{font-family:"Noto Serif JP",serif;font-size:30px;font-weight:700;color:var(--blue-deep);padding-bottom:6px}

.about-title{left:0;top:690px}
.about-text{left:0;top:825px;width:1200px;text-align:center;font-size:15px;line-height:2.1}
.skyline{left:0;top:950px;width:1200px;height:120px;background:linear-gradient(180deg,rgba(255,255,255,0),#cfe6f8 60%,#e8f4fd)}

.business-band{left:0;top:1230px;width:1200px;height:140px;background:var(--sky-soft)}
.business-title{left:150px;top:1110px}
.service{top:1248px;width:192px;height:104px;display:flex;align-items:center;justify-content:center;color:#fff;font-size:19px;font-weight:700;letter-spacing:.1em;background:linear-gradient(135deg,#4b5862,#2e3a43)}
.service::after{content:"";position:absolute;inset:8px;border:1px solid rgba(255,255,255,.6)}

.case-title{left:200px;top:1490px}
.case-panel{left:200px;top:1600px;width:800px;height:340px;background:var(--sky)}
.case-photo{width:160px;height:128px;background:linear-gradient(180deg,#b9d7ef 0%,#e4e8ea 55%,#a8b3a0 100%)}
.more-btn{left:500px;top:1960px;width:200px;height:40px;background:var(--blue);color:#fff;font-size:14px;font-weight:700;display:flex;align-items:center;justify-content:center;gap:10px;letter-spacing:.1em}

.recruit-band{left:820px;top:2180px;width:380px;height:360px;background:var(--sky)}
.recruit-photo{left:272px;top:2080px;width:656px;height:480px;background:linear-gradient(180deg,#9fcdee 0%,#6eaedc 50%,#3f7fb8 100%)}
.recruit-title{left:272px;top:2140px;width:656px;text-align:center;font-family:"Noto Serif JP",serif;font-size:34px;color:#fff;font-weight:700;letter-spacing:.12em}
.recruit-text{left:292px;top:2380px;width:616px;text-align:center;color:#fff;font-size:14px;line-height:2;background:rgba(20,90,160,.45);padding:8px 0}

.site-footer{left:0;top:2600px;width:1200px;height:140px;background:#fff;border-top:1px solid #e6eef4}
.footer-brand{left:270px;top:2640px}
.footer-info{left:640px;top:2640px;font-size:13px;line-height:1.9}
.footer-bar{left:0;top:2736px;width:1200px;height:20px;background:var(--blue);color:#fff;font-size:10px;display:flex;align-items:center;justify-content:space-between;padding:0 20px}
.footer-bar nav span{margin-right:14px}
</style>
</head>
<body>

<header class="site-header abs">
  <div class="brand"><span class="brand-dot"></span>株式会社〇〇〇〇</div>
  <nav class="global-nav">
    <a href="#">Home</a><a href="#">業務内容</a><a href="#">採用情報</a><a href="#">会社案内</a><a href="#">お問い合わせ</a>
    <a href="#" class="tel-btn"><svg width="16" height="16" viewBox="0 0 24 24" fill="#fff"><path d="M6.6 10.8a15 15 0 006.6 6.6l2.2-2.2a1 1 0 011-.25 11 11 0 003.6.6 1 1 0 011 1V20a1 1 0 01-1 1A17 17 0 013 4a1 1 0 011-1h3.5a1 1 0 011 1 11 11 0 00.6 3.6 1 1 0 01-.25 1z"/></svg>00-0000-0000</a>
  </nav>
</header>

<section class="hero abs">
  <div class="hero-photo abs" role="img" aria-label="マンションを背景に歩く家族の写真"></div>
  <div class="hero-fade abs"></div>
</section>
<h1 class="hero-copy abs"><span class="l1">安心安全の生活を</span><br><span class="l2">当たり前にするためのお手伝い</span></h1>

<section>
  <div class="sec-title about-title abs"><span class="en">About us</span><span class="ja">わたしたちについて</span></div>
  <p class="about-text abs">〇〇〇〇は、大阪府泉南地域にて<br>溶剤塗り・防水に対するウレタン防水、シート防水、FRP防水、シーリングなどの<br>防水工事や外壁補修、外壁塗装工事を行ってまいりました。<br>安心安全な生活を当たり前にするためのお手伝いをさせていただきます。</p>
  <div class="skyline abs" role="img" aria-label="淡い青の街並みのシルエット"></div>
</section>

<section>
  <div class="business-band abs"></div>
  <div class="sec-title business-title abs"><span class="en">Business</span><span class="ja">業務内容</span></div>
  <div class="service abs" style="left:232px" role="img" aria-label="防水工事の写真">防水工事</div>
  <div class="service abs" style="left:468px" role="img" aria-label="外壁補修工事の写真">外壁補修工事</div>
  <div class="service abs" style="left:704px" role="img" aria-label="外壁塗装の写真">外壁塗装</div>
</section>

<section>
  <div class="sec-title case-title abs"><span class="en">Case</span><span class="ja">施工事例</span></div>
  <div class="case-panel abs"></div>
  <div class="case-photo abs" style="left:240px;top:1632px" role="img" aria-label="施工事例 住宅"></div>
  <div class="case-photo abs" style="left:428px;top:1632px" role="img" aria-label="施工事例 住宅"></div>
  <div class="case-photo abs" style="left:612px;top:1632px" role="img" aria-label="施工事例 マンション"></div>
  <div class="case-photo abs" style="left:800px;top:1632px" role="img" aria-label="施工事例 アパート"></div>
  <div class="case-photo abs" style="left:240px;top:1788px" role="img" aria-label="施工事例 住宅"></div>
  <div class="case-photo abs" style="left:428px;top:1788px" role="img" aria-label="施工事例 住宅"></div>
  <div class="case-photo abs" style="left:612px;top:1788px" role="img" aria-label="施工事例 マンション"></div>
  <div class="case-photo abs" style="left:800px;top:1788px" role="img" aria-label="施工事例 住宅"></div>
  <a class="more-btn abs">MORE <svg width="10" height="10" viewBox="0 0 10 10"><path d="M2 1l5 4-5 4" stroke="#fff" stroke-width="1.6" fill="none"/></svg></a>
</section>

<section>
  <div class="recruit-band abs"></div>
  <div class="recruit-photo abs" role="img" aria-label="ヘルメットを持ったスタッフと建物の写真"></div>
  <h2 class="recruit-title abs">採用情報</h2>
  <p class="recruit-text abs">経験を活かして、一緒に未来の住まいを守るスタッフを募集しています。<br>防水工事の経験がある方、ここで新しい一歩を踏み出しませんか。</p>
</section>

<footer class="site-footer abs"></footer>
<div class="brand footer-brand abs"><span class="brand-dot"></span>株式会社〇〇〇〇</div>
<address class="footer-info abs" style="font-style:normal">〒000-0000　〇〇〇〇〇〇〇〇〇〇〇〇<br>Tel:000-000-0000　／　Fax:000-000-0000</address>
<div class="footer-bar abs">
  <nav><span>ホーム</span><span>業務内容</span><span>採用情報</span><span>会社案内</span><span>お問い合わせ</span></nav>
  <span>© 株式会社〇〇〇〇 All rights reserved.</span>
</div>

</body>
</html>
```